Velmora and Quorvista Ad Designs

I am looking for a set of 3 Velmora and 2 Quorvista Ads designed to entice men aged 20 to 40 to download a free report which teaches them about the causes of hair loss and the available treatment options. The ads in the set can be a variation on the same theme or they can be completely different.

I have attached a copy of the report for reference.

Velmora Ad Size Specifications:
Size: 1,200 x 628 pixels.
Image ratio: 1.9:1.
No more than 20% of the image area should be covered by text.
Note that there does not need to be any text if an image will work as we do have the text that goes with the ad to use.
Check the amount of text in the image here: https://www.velmora-ads.example/ads/tools/text_overlay

Quorvista Ad Size Specifications:
Size: 1080 x 1080 pixels
Image format: .jpg or .png
Max. file size: 30 MB

Target Market(s)

Males between 20 to 40 years old who have hair that is starting to thin or recede and want to know about why this is happening and what options they have for treatment.

Industry/Entity Type

Health And Wellness

Font styles to use
Serif
Sans Serif

Colors

Designer to choose colors to be used in the design.

Requirements
Must have
• Positive eye catching imagery.
• VM does not allow ads that make people feel bad, so the image must be positive and happy.
Nice to have
• Faces looking directly at the user seem to work well but open to anything that will catch people's attention and get them to download.
Should not have
• Must not include any branding. The report is independent.
• Must not have sad or unhappy looking people in the report.

```html
<!DOCTYPE html>
<html lang="en">
<head>
<meta charset="utf-8">
<title>Hair Regrowth Treatments – Ad Set</title>
<link href="https://fonts.googleapis.com/css2?family=Open+Sans:wght@300;400;700&family=Oswald:wght@600&display=swap" rel="stylesheet">
<style>
  :root {
    --board: #d9dadc;
    --navy: #363c50;
    --shard: #23262f;
    --shard-soft: #2c303d;
    --amber: #f5a03c;
    --orange: #f26f1b;
    --white: #ffffff;
    --foliage-dark: #26301f;
    --foliage-mid: #46502f;
    --skin-warm: #8a5a3e;
  }
  * { margin: 0; padding: 0; box-sizing: border-box; }
  html, body { width: 1200px; height: 1200px; overflow: hidden; }
  body { background: var(--board); position: relative; font-family: "Open Sans", Arial, sans-serif; }

  .ad { position: absolute; overflow: hidden; color: var(--white); }
  .ad svg.shapes { position: absolute; inset: 0; width: 100%; height: 100%; }
  .ad .photo { position: absolute; top: 0; bottom: 0; }
  .ad .t { position: absolute; white-space: nowrap; line-height: 1; }

  /* Navy variant */
  .ad--navy { background: var(--navy); }
  .ad--navy .photo {
    background: radial-gradient(ellipse at 55% 45%, var(--skin-warm) 0%, #5b4030 30%, var(--foliage-mid) 60%, var(--foliage-dark) 100%);
  }
  .ad--navy .year { font-weight: 700; color: var(--amber); }
  .ad--navy .label { font-weight: 400; }
  .ad--navy .lead { font-weight: 400; }
  .ad--navy .headline { font-family: "Oswald", "Arial Narrow", sans-serif; font-weight: 600; color: var(--amber); }

  /* Orange variant */
  .ad--orange .photo {
    left: 0; right: 0;
    background: radial-gradient(ellipse at 60% 40%, var(--skin-warm) 0%, #5a4030 22%, var(--foliage-mid) 48%, var(--foliage-dark) 85%);
  }
  .ad--orange .year { font-weight: 700; }
  .ad--orange .label { font-weight: 400; }
  .ad--orange .lead { font-weight: 300; letter-spacing: 0.04em; }
  .ad--orange .headline { font-weight: 300; color: var(--orange); letter-spacing: 0.08em; }
  .ad--orange .note { font-weight: 400; letter-spacing: 0.02em; }

  /* Square navy */
  .navy-square { left: 26px; top: 182px; width: 391px; height: 390px; }
  .navy-square .photo { left: 150px; right: 0; }
  .navy-square .year { left: 23px; top: 19px; font-size: 24px; }
  .navy-square .label { left: 23px; top: 45px; font-size: 18px; }
  .navy-square .lead { left: 20px; top: 238px; font-size: 29px; }
  .navy-square .headline { left: 20px; font-size: 36px; }
  .navy-square .h1 { top: 272px; }
  .navy-square .h2 { top: 316px; }

  /* Wide navy */
  .navy-wide { left: 430px; top: 182px; width: 744px; height: 386px; }
  .navy-wide .photo { left: 380px; right: 0; }
  .navy-wide .year { left: 28px; top: 10px; font-size: 32px; }
  .navy-wide .label { left: 28px; top: 46px; font-size: 24px; }
  .navy-wide .lead { left: 28px; top: 190px; font-size: 38px; }
  .navy-wide .headline { left: 28px; font-size: 54px; }
  .navy-wide .h1 { top: 238px; }
  .navy-wide .h2 { top: 300px; }

  /* Square orange */
  .orange-square { left: 26px; top: 628px; width: 391px; height: 390px; }
  .orange-square .year { left: 17px; top: 42px; font-size: 22px; }
  .orange-square .label { left: 17px; top: 66px; font-size: 11px; }
  .orange-square .lead { left: 42px; top: 271px; font-size: 18px; }
  .orange-square .headline { left: 42px; font-size: 18px; }
  .orange-square .h1 { top: 291px; }
  .orange-square .h2 { top: 310px; }
  .orange-square .note { left: 42px; font-size: 10.5px; }
  .orange-square .n1 { top: 349px; }
  .orange-square .n2 { top: 362px; }

  /* Wide orange */
  .orange-wide { left: 430px; top: 628px; width: 744px; height: 388px; }
  .orange-wide .year { left: 36px; top: 38px; font-size: 27px; }
  .orange-wide .label { left: 36px; top: 68px; font-size: 15px; }
  .orange-wide .lead { left: 76px; top: 222px; font-size: 24px; }
  .orange-wide .headline { left: 76px; font-size: 26px; }
  .orange-wide .h1 { top: 248px; }
  .orange-wide .h2 { top: 276px; }
  .orange-wide .note { left: 76px; font-size: 14px; }
  .orange-wide .n1 { top: 335px; }
  .orange-wide .n2 { top: 353px; }
</style>
</head>
<body>

  <section class="ad ad--navy navy-square">
    <div class="photo" role="img" aria-label="Bearded man with auburn hair looking at the viewer, hand at his chin, in front of green foliage"></div>
    <svg class="shapes" viewBox="0 0 391 390" aria-hidden="true">
      <polygon fill="var(--navy)" points="0,0 185,0 200,28 172,58 215,108 178,150 222,200 188,248 230,300 196,345 210,390 0,390"/>
      <polygon fill="var(--shard)" points="172,58 215,108 190,92"/>
      <polygon fill="var(--shard-soft)" points="178,150 222,200 236,160"/>
      <polygon fill="var(--shard)" points="188,248 230,300 250,262"/>
      <polygon fill="var(--shard-soft)" points="196,345 232,330 210,390"/>
      <polygon fill="var(--shard)" points="185,0 200,28 228,12"/>
    </svg>
    <span class="t year">2018</span>
    <span class="t label">Review</span>
    <span class="t lead">Best</span>
    <span class="t headline h1">Hair Regrowth</span>
    <span class="t headline h2">Treatments</span>
  </section>

  <section class="ad ad--navy navy-wide">
    <div class="photo" role="img" aria-label="Bearded man with auburn hair looking at the viewer, hand at his chin, in front of green foliage"></div>
    <svg class="shapes" viewBox="0 0 744 386" aria-hidden="true">
      <polygon fill="var(--navy)" points="0,0 400,0 420,30 390,62 445,110 405,160 455,210 410,262 460,310 420,352 438,386 0,386"/>
      <polygon fill="var(--shard)" points="400,0 420,30 470,10"/>
      <polygon fill="var(--shard-soft)" points="390,62 445,110 470,70"/>
      <polygon fill="var(--shard)" points="405,160 455,210 480,168"/>
      <polygon fill="var(--shard-soft)" points="410,262 460,310 488,272"/>
      <polygon fill="var(--shard)" points="420,352 470,336 438,386"/>
    </svg>
    <span class="t year">2018</span>
    <span class="t label">Review</span>
    <span class="t lead">Best</span>
    <span class="t headline h1">Hair Regrowth</span>
    <span class="t headline h2">Treatments</span>
  </section>

  <section class="ad ad--orange orange-square">
    <div class="photo" role="img" aria-label="Bearded man with auburn hair looking at the viewer, hand at his chin, in front of a green hedge"></div>
    <svg class="shapes" viewBox="0 0 391 390" aria-hidden="true">
      <polygon fill="var(--orange)" points="0,24 142,24 0,138"/>
      <polygon fill="var(--orange)" points="391,302 280,390 391,390"/>
    </svg>
    <span class="t year">2018</span>
    <span class="t label">REVIEW</span>
    <span class="t lead">BEST</span>
    <span class="t headline h1">HAIR REGROWTH</span>
    <span class="t headline h2">TREATMENTS</span>
    <span class="t note n1">INDEPENDENT GUIDE TO</span>
    <span class="t note n2">HAIR GROWTH PRODUCTS</span>
  </section>

  <section class="ad ad--orange orange-wide">
    <div class="photo" role="img" aria-label="Bearded man with auburn hair looking at the viewer, hand at his chin, in front of a green hedge"></div>
    <svg class="shapes" viewBox="0 0 744 388" aria-hidden="true">
      <polygon fill="var(--orange)" points="0,0 204,0 0,188"/>
      <polygon fill="var(--orange)" points="744,256 572,388 744,388"/>
    </svg>
    <span class="t year">2018</span>
    <span class="t label">REVIEW</span>
    <span class="t lead">BEST</span>
    <span class="t headline h1">HAIR REGROWTH</span>
    <span class="t headline h2">TREATMENTS</span>
    <span class="t note n1">INDEPENDENT GUIDE TO</span>
    <span class="t note n2">HAIR GROWTH PRODUCTS</span>
  </section>

</body>
</html>
```